Bathroom Renovation Business card design needed

Bathroom, Kitchen & Laundry Renovations
Mainly complete bathroom renovations

Target Market(s)

people wanting a total bathroom renovations and other trades people

Industry/Entity Type

Business

Contact Information for Business Card

Dalby Bathrooms
Tomas Dalby
Mobile: 0438 207615
Licence no: 764519K
Email: dalbybathrooms@mailnest.example

Logo styles of interest
Lettermark Logo
Requirements
Must have
• the business card should be predominantly blue
Nice to have
• the DB logo featured in the business card will be used on tshirts,tax invoices , letters etc so the DB will be the main feature, and preferably blue
Should not have
• We found the red DB logo through google images. We understand that it cannot be exactly the same but we like how the DB is linked. The example business card is something we designed but we prefer more blues. Maybe different shades of blue.

```html
<!DOCTYPE html>
<html lang="en">
<head>
<meta charset="utf-8">
<title>Dalby Bathrooms – Business Card</title>
<link rel="stylesheet" href="https://fonts.googleapis.com/css2?family=Kanit:ital,wght@0,300;1,300;1,400&display=swap">
<style>
  :root {
    --blue-deep: #0e6580;
    --blue-mid: #1c7c9c;
    --blue-light: #2a8bac;
    --ink: #ffffff;
  }
  html, body {
    margin: 0;
    padding: 0;
    overflow: hidden;
  }
  .card {
    position: relative;
    width: 1200px;
    height: 694px;
    overflow: hidden;
    background: linear-gradient(90deg, var(--blue-deep) 0%, var(--blue-mid) 45%, var(--blue-light) 100%);
    font-family: "Kanit", sans-serif;
    color: var(--ink);
  }
  .rule {
    position: absolute;
    top: 171px;
    height: 3px;
  }
  .rule--left { left: 0; width: 312px; }
  .rule--right { left: 889px; width: 311px; }
  .line {
    position: absolute;
    left: 0;
    width: 100%;
    text-align: center;
    line-height: 1;
    white-space: nowrap;
  }
  .company {
    top: 140px;
    font-size: 58px;
    font-weight: 300;
    letter-spacing: 1px;
  }
  .owner {
    top: 214px;
    font-size: 62px;
    font-weight: 400;
    font-style: italic;
  }
  .phone {
    top: 355px;
    font-size: 52px;
    font-weight: 300;
  }
  .email {
    top: 413px;
    font-size: 52px;
    font-weight: 300;
  }
  .licence {
    top: 506px;
    font-size: 45px;
    font-weight: 300;
  }
</style>
</head>
<body>
  <div class="card">
    <svg class="rule rule--left" viewBox="0 0 312 3" preserveAspectRatio="none" aria-hidden="true">
      <line x1="0" y1="1.5" x2="312" y2="1.5" stroke="#ffffff" stroke-width="2.5" stroke-dasharray="6 5"/>
    </svg>
    <svg class="rule rule--right" viewBox="0 0 311 3" preserveAspectRatio="none" aria-hidden="true">
      <line x1="0" y1="1.5" x2="311" y2="1.5" stroke="#ffffff" stroke-width="2.5" stroke-dasharray="6 5"/>
    </svg>

    <div class="line company">Dalby Bathrooms</div>
    <div class="line owner">Tomas Dalby</div>
    <div class="line phone">0438 207 615</div>
    <div class="line email">dalbybathrooms@mailnest.example</div>
    <div class="line licence">Lic No: 764519K</div>
  </div>
</body>
</html>
```